Flyers

Modify Existing Flyer and create another for exterior company
Updates

Previous Brief has been updated- we want to update this existing one also

Target Market(s)

Exterior Remodeling Customers

Industry/Entity Type

Remodeling/Construction

```html
<!DOCTYPE html>
<html lang="en">
<head>
<meta charset="utf-8">
<title>Northgate Roofing and Exteriors – Remodeling Flyer</title>
<link href="https://fonts.googleapis.com/css2?family=Fira+Sans+Condensed:wght@700;800&family=Hind:wght@400;500&family=Montserrat:wght@500;800&family=Signika:wght@600&display=swap" rel="stylesheet">
<style>
  :root{
    --orange:#ef5a24;
    --blue:#0a6fc9;
    --black:#0c0c0c;
    --white:#ffffff;
    --ink:#222428;
  }
  *{box-sizing:border-box;margin:0;padding:0}
  html,body{width:1027px;height:1200px;overflow:hidden;background:var(--white)}
  .flyer{position:relative;width:1027px;height:1200px;font-family:"Hind",sans-serif;color:var(--ink);overflow:hidden}

  .header{position:absolute;left:0;top:0;width:100%;height:150px}
  .header svg{position:absolute;inset:0}
  .headline{position:absolute;left:50px;top:22px;font-family:"Signika",sans-serif;font-weight:600;font-size:32px;line-height:1.2;color:var(--white)}
  .headline span{display:block}
  .headline .l2{padding-left:8px}
  .headline .l3{padding-left:14px}
  .brand{position:absolute;left:640px;top:36px;width:350px;text-align:center;color:var(--white)}
  .brand-name{font-family:"Montserrat",sans-serif;font-weight:800;font-size:42px;letter-spacing:2px;color:var(--orange);line-height:1}
  .brand-sub{margin-top:10px;font-family:"Montserrat",sans-serif;font-weight:500;font-size:16px;letter-spacing:.5px;border-top:2px solid var(--blue);border-bottom:2px solid var(--blue);padding:5px 0 3px}

  .hero{position:absolute;left:0;top:150px;width:100%;height:320px}
  .hero svg{position:absolute;inset:0}

  .banner{position:absolute;left:0;top:455px;width:700px;height:100px}
  .banner svg{position:absolute;inset:0}
  .banner-text{position:absolute;left:58px;top:14px;font-family:"Fira Sans Condensed",sans-serif;font-weight:800;font-size:31px;line-height:1.22;color:var(--white);text-transform:uppercase}

  .service{position:absolute}
  .service h2{font-family:"Fira Sans Condensed",sans-serif;font-weight:800;font-size:22px;color:var(--orange);text-transform:uppercase;line-height:22px}
  .service p{font-size:14px;line-height:18px;margin-top:6px}
  .service .icon{position:absolute;left:-50px;top:0}
  .ticks{list-style:none;margin-top:8px}
  .ticks li{position:relative;padding-left:20px;font-size:14px;line-height:21px}
  .ticks li svg{position:absolute;left:0;top:4px}
  .ticks.wrap li{line-height:18px;margin-bottom:3px}
  .just{text-align:justify}

  .kitchen{left:118px;top:572px;width:420px}
  .bathroom{left:118px;top:852px;width:420px}
  .bathroom .ticks{width:220px}
  .additions{left:660px;top:572px;width:340px}
  .decks{left:660px;top:842px;width:340px}
  .decks .ticks{width:150px}

  .thumb{position:absolute}
  .thumb-kitchen{left:372px;top:712px;width:163px;height:120px}
  .thumb-bath{left:372px;top:945px;width:163px;height:135px}
  .thumb-bedroom{left:822px;top:690px;width:170px;height:130px}
  .thumb-patio{left:830px;top:962px;width:165px;height:118px}

  .footer{position:absolute;left:0;top:1110px;width:100%;height:90px}
  .footer svg.band{position:absolute;inset:0}
  .call{position:absolute;left:58px;top:16px;font-family:"Fira Sans Condensed",sans-serif;font-weight:700;font-size:25px;line-height:1.15;color:var(--white);text-transform:uppercase}
  .call .phone{text-transform:none}
  .call svg{vertical-align:-2px;margin:0 4px}
  .web{position:absolute;left:655px;top:32px;font-size:23px;font-weight:500;color:var(--white);display:flex;align-items:center;gap:10px}
</style>
</head>
<body>
<div class="flyer">

  <header class="header">
    <svg width="1027" height="150" viewBox="0 0 1027 150">
      <rect width="1027" height="150" fill="var(--black)"/>
      <polygon points="0,0 555,0 612,150 0,150" fill="var(--orange)"/>
    </svg>
    <h1 class="headline">
      <span>Ready for</span>
      <span class="l2">a Beautiful and Functional</span>
      <span class="l3">Kitchen or Bathroom?</span>
    </h1>
    <div class="brand">
      <div class="brand-name">NORTHGATE</div>
      <div class="brand-sub">ROOFING AND EXTERIORS</div>
    </div>
  </header>

  <section class="hero">
    <svg width="1027" height="320" viewBox="0 0 1027 320">
      <defs>
        <linearGradient id="kitchenGrad" x1="0" y1="0" x2="1" y2="1">
          <stop offset="0" stop-color="#f7f3ec"/>
          <stop offset="1" stop-color="#d8ccb8"/>
        </linearGradient>
        <linearGradient id="bathGrad" x1="0" y1="0" x2="1" y2="1">
          <stop offset="0" stop-color="#a9b4bd"/>
          <stop offset="1" stop-color="#ece9e4"/>
        </linearGradient>
      </defs>
      <polygon points="0,0 490,0 616,320 0,320" fill="url(#kitchenGrad)" role="img" aria-label="Photo of a bright white remodeled kitchen with island and pendant lights"/>
      <polygon points="498,0 1027,0 1027,320 624,320" fill="url(#bathGrad)" role="img" aria-label="Photo of a remodeled bathroom with marble vanity and glass tile shower"/>
      <polygon points="490,0 498,0 624,320 616,320" fill="var(--white)"/>
    </svg>
  </section>

  <div class="banner">
    <svg width="700" height="100" viewBox="0 0 700 100">
      <polygon points="0,0 672,0 700,100 0,100" fill="var(--blue)"/>
    </svg>
    <div class="banner-text">Work with a top-rated local<br>remodeling company in Ankeny, IA</div>
  </div>

  <section class="service kitchen">
    <svg class="icon" width="40" height="40" viewBox="0 0 44 44" fill="none" stroke="var(--blue)" stroke-width="2">
      <rect x="4" y="20" width="36" height="20"/><rect x="9" y="27" width="12" height="9"/><line x1="28" y1="26" x2="35" y2="26"/>
      <path d="M8 14h10l-2-6H10z" stroke="var(--orange)"/><line x1="30" y1="4" x2="30" y2="16" stroke="var(--orange)"/>
    </svg>
    <h2>Kitchen Remodeling</h2>
    <p>Whatever your vision is for your new kitchen, our crew can help you bring it to life. You can trust us for:</p>
    <ul class="ticks">
      <li><svg width="13" height="13" viewBox="0 0 13 13"><circle cx="6.5" cy="6.5" r="6.5" fill="var(--blue)"/><path d="M3.5 6.8l2 2 4-4.2" stroke="#fff" stroke-width="1.6" fill="none"/></svg>Open concept design services</li>
      <li><svg width="13" height="13" viewBox="0 0 13 13"><circle cx="6.5" cy="6.5" r="6.5" fill="var(--blue)"/><path d="M3.5 6.8l2 2 4-4.2" stroke="#fff" stroke-width="1.6" fill="none"/></svg>Kitchen cabinet installation services</li>
      <li><svg width="13" height="13" viewBox="0 0 13 13"><circle cx="6.5" cy="6.5" r="6.5" fill="var(--blue)"/><path d="M3.5 6.8l2 2 4-4.2" stroke="#fff" stroke-width="1.6" fill="none"/></svg>Kitchen countertop installation services</li>
      <li><svg width="13" height="13" viewBox="0 0 13 13"><circle cx="6.5" cy="6.5" r="6.5" fill="var(--blue)"/><path d="M3.5 6.8l2 2 4-4.2" stroke="#fff" stroke-width="1.6" fill="none"/></svg>Tile installation services</li>
      <li><svg width="13" height="13" viewBox="0 0 13 13"><circle cx="6.5" cy="6.5" r="6.5" fill="var(--blue)"/><path d="M3.5 6.8l2 2 4-4.2" stroke="#fff" stroke-width="1.6" fill="none"/></svg>Lighting installation services</li>
      <li><svg width="13" height="13" viewBox="0 0 13 13"><circle cx="6.5" cy="6.5" r="6.5" fill="var(--blue)"/><path d="M3.5 6.8l2 2 4-4.2" stroke="#fff" stroke-width="1.6" fill="none"/></svg>Plumbing upgrade services</li>
      <li><svg width="13" height="13" viewBox="0 0 13 13"><circle cx="6.5" cy="6.5" r="6.5" fill="var(--blue)"/><path d="M3.5 6.8l2 2 4-4.2" stroke="#fff" stroke-width="1.6" fill="none"/></svg>Electrical upgrade services</li>
      <li><svg width="13" height="13" viewBox="0 0 13 13"><circle cx="6.5" cy="6.5" r="6.5" fill="var(--blue)"/><path d="M3.5 6.8l2 2 4-4.2" stroke="#fff" stroke-width="1.6" fill="none"/></svg>Drywall services</li>
      <li><svg width="13" height="13" viewBox="0 0 13 13"><circle cx="6.5" cy="6.5" r="6.5" fill="var(--blue)"/><path d="M3.5 6.8l2 2 4-4.2" stroke="#fff" stroke-width="1.6" fill="none"/></svg>Painting services</li>
    </ul>
  </section>
  <div class="thumb thumb-kitchen" role="img" aria-label="Photo of a kitchen with grey island and wood floor" style="background:linear-gradient(135deg,#eef0f1,#8a8f94)"></div>

  <section class="service bathroom">
    <svg class="icon" width="40" height="40" viewBox="0 0 44 44" fill="none" stroke="var(--blue)" stroke-width="2">
      <rect x="18" y="4" width="18" height="12" stroke="var(--orange)"/><path d="M4 24h36M8 24v12h28V24M14 36v5M30 36v5"/>
    </svg>
    <h2>Bathroom Remodeling</h2>
    <p class="just">When you hire us for your bathroom remodeling project, the possibilities are endless. Our experienced and talented team can:</p>
    <ul class="ticks wrap">
      <li><svg width="13" height="13" viewBox="0 0 13 13"><circle cx="6.5" cy="6.5" r="6.5" fill="var(--blue)"/><path d="M3.5 6.8l2 2 4-4.2" stroke="#fff" stroke-width="1.6" fill="none"/></svg>Install a custom tile shower</li>
      <li><svg width="13" height="13" viewBox="0 0 13 13"><circle cx="6.5" cy="6.5" r="6.5" fill="var(--blue)"/><path d="M3.5 6.8l2 2 4-4.2" stroke="#fff" stroke-width="1.6" fill="none"/></svg>Build a new vanity</li>
      <li><svg width="13" height="13" viewBox="0 0 13 13"><circle cx="6.5" cy="6.5" r="6.5" fill="var(--blue)"/><path d="M3.5 6.8l2 2 4-4.2" stroke="#fff" stroke-width="1.6" fill="none"/></svg>Install flooring and tile</li>
      <li><svg width="13" height="13" viewBox="0 0 13 13"><circle cx="6.5" cy="6.5" r="6.5" fill="var(--blue)"/><path d="M3.5 6.8l2 2 4-4.2" stroke="#fff" stroke-width="1.6" fill="none"/></svg>Replace your plumbing and light fixtures</li>
    </ul>
  </section>
  <div class="thumb thumb-bath" role="img" aria-label="Photo of a bathroom with glass shower and freestanding tub" style="background:linear-gradient(135deg,#b9bec3,#eceae7)"></div>

  <section class="service additions">
    <svg class="icon" width="42" height="40" viewBox="0 0 46 44" fill="none" stroke="var(--blue)" stroke-width="2">
      <path d="M4 20L23 5l19 15" stroke="var(--orange)"/><path d="M8 17v23h30V17"/><rect x="19" y="27" width="8" height="13"/><rect x="11" y="22" width="6" height="6"/><rect x="29" y="22" width="6" height="6"/>
    </svg>
    <h2>Home Additions</h2>
    <p>No matter what kind of space you need, our team will bring your vision to life. You can hire us if you need a:</p>
    <ul class="ticks">
      <li><svg width="13" height="13" viewBox="0 0 13 13"><circle cx="6.5" cy="6.5" r="6.5" fill="var(--blue)"/><path d="M3.5 6.8l2 2 4-4.2" stroke="#fff" stroke-width="1.6" fill="none"/></svg>Bathroom addition</li>
      <li><svg width="13" height="13" viewBox="0 0 13 13"><circle cx="6.5" cy="6.5" r="6.5" fill="var(--blue)"/><path d="M3.5 6.8l2 2 4-4.2" stroke="#fff" stroke-width="1.6" fill="none"/></svg>Bedroom addition</li>
      <li><svg width="13" height="13" viewBox="0 0 13 13"><circle cx="6.5" cy="6.5" r="6.5" fill="var(--blue)"/><path d="M3.5 6.8l2 2 4-4.2" stroke="#fff" stroke-width="1.6" fill="none"/></svg>Garage addition</li>
      <li><svg width="13" height="13" viewBox="0 0 13 13"><circle cx="6.5" cy="6.5" r="6.5" fill="var(--blue)"/><path d="M3.5 6.8l2 2 4-4.2" stroke="#fff" stroke-width="1.6" fill="none"/></svg>Basement addition</li>
      <li><svg width="13" height="13" viewBox="0 0 13 13"><circle cx="6.5" cy="6.5" r="6.5" fill="var(--blue)"/><path d="M3.5 6.8l2 2 4-4.2" stroke="#fff" stroke-width="1.6" fill="none"/></svg>Guest room addition</li>
      <li><svg width="13" height="13" viewBox="0 0 13 13"><circle cx="6.5" cy="6.5" r="6.5" fill="var(--blue)"/><path d="M3.5 6.8l2 2 4-4.2" stroke="#fff" stroke-width="1.6" fill="none"/></svg>Living room addition</li>
      <li><svg width="13" height="13" viewBox="0 0 13 13"><circle cx="6.5" cy="6.5" r="6.5" fill="var(--blue)"/><path d="M3.5 6.8l2 2 4-4.2" stroke="#fff" stroke-width="1.6" fill="none"/></svg>Sunroom addition</li>
    </ul>
  </section>
  <div class="thumb thumb-bedroom" role="img" aria-label="Photo of a bright bedroom addition with large windows" style="background:linear-gradient(135deg,#f2f2f0,#a7aaad)"></div>

  <section class="service decks">
    <svg class="icon" width="40" height="40" viewBox="0 0 44 44" fill="none" stroke="var(--blue)" stroke-width="2">
      <path d="M6 16a16 12 0 0 1 32 0z" stroke="var(--orange)"/><line x1="22" y1="16" x2="22" y2="36"/><path d="M4 30h36M10 30v10M34 30v10"/>
    </svg>
    <h2>Decks/Patios</h2>
    <p class="just">An outdoor space is a great addition to any residential property. When you decide to build a patio or deck, you'll be able to experience a variety of benefits. Your outdoor area will increase your:</p>
    <ul class="ticks">
      <li><svg width="13" height="13" viewBox="0 0 13 13"><circle cx="6.5" cy="6.5" r="6.5" fill="var(--blue)"/><path d="M3.5 6.8l2 2 4-4.2" stroke="#fff" stroke-width="1.6" fill="none"/></svg>Property value</li>
      <li><svg width="13" height="13" viewBox="0 0 13 13"><circle cx="6.5" cy="6.5" r="6.5" fill="var(--blue)"/><path d="M3.5 6.8l2 2 4-4.2" stroke="#fff" stroke-width="1.6" fill="none"/></svg>Curb appeal</li>
      <li><svg width="13" height="13" viewBox="0 0 13 13"><circle cx="6.5" cy="6.5" r="6.5" fill="var(--blue)"/><path d="M3.5 6.8l2 2 4-4.2" stroke="#fff" stroke-width="1.6" fill="none"/></svg>Functional living</li>
      <li><svg width="13" height="13" viewBox="0 0 13 13"><circle cx="6.5" cy="6.5" r="6.5" fill="var(--blue)"/><path d="M3.5 6.8l2 2 4-4.2" stroke="#fff" stroke-width="1.6" fill="none"/></svg>Space</li>
    </ul>
  </section>
  <div class="thumb thumb-patio" role="img" aria-label="Photo of a covered wooden deck with outdoor dining set" style="background:linear-gradient(135deg,#b98a5c,#6f8f55)"></div>

  <footer class="footer">
    <svg class="band" width="1027" height="90" viewBox="0 0 1027 90">
      <polygon points="0,0 600,0 630,90 0,90" fill="var(--blue)"/>
      <polygon points="600,0 1027,0 1027,90 630,90" fill="var(--orange)"/>
    </svg>
    <div class="call">Call today for your<br>free estimate<svg width="20" height="20" viewBox="0 0 20 20"><circle cx="10" cy="10" r="9" fill="none" stroke="#fff" stroke-width="1.8"/><path d="M7 5.5l2 2-1 1.5c.6 1.4 1.6 2.4 3 3l1.5-1 2 2-1.2 1.5c-3.5-.3-7-3.8-7.3-7.3z" fill="#fff"/></svg><span class="phone">555-014-2837</span></div>
    <div class="web">
      <svg width="24" height="24" viewBox="0 0 24 24" fill="none" stroke="#fff" stroke-width="1.6"><circle cx="12" cy="12" r="10"/><ellipse cx="12" cy="12" rx="4.5" ry="10"/><line x1="2" y1="12" x2="22" y2="12"/></svg>
      www.northgateremodel.com
    </div>
  </footer>

</div>
</body>
</html>
```